Website for the recruitment firm vorl

Objective :

Create a modern, elegant, and understated website with a touch of sophistication. The site must be fully custom-coded (or custom-coded on WordPress), responsive, and fast, reflecting the quality and high standards of our firm.

It must be bilingual (FR/EN), with a language selector visible in the header.

About vorl.

vorl. is a high-end recruitment firm, led by experienced consultants—employees and freelancers—and supported by a dedicated team of recruitment managers. Our hybrid approach allows us to handle complex, confidential, or high-volume projects with rigor and agility.

We operate across several business verticals:

Executive

Finance & Advisory (accounting, management control, treasury, corporate finance, financial consulting or investment banking)

Legal

Audit & Expertise

People & Office

Supply & Purchasing

Industry & Engineering

Our approach is based on a balance between human know-how and cutting-edge technologies (AI, automation, data) to respond to recruitment challenges with accuracy, responsiveness and impact.

Slogan: Expertise at the service of every recruitment.

Purpose of the site:

Client side: present our expertise, our values, our support.

Candidate side: allow the search for offers, by expertise.

On the consultant side: encouraging freelancers or employees to join us.

Structure & pages requested:

Welcome

Main banner with slogan and strong visual (possibility of a background video like maltevo.ca — for a modern and dynamic look)

Clear redirection to both paths: “I’m looking for talent” / “I want to join vorl. ”

Quick presentation of expertise with redirection to each dedicated page

Highlighting values

About

Our mission

Our values (excellence, flexibility, partnership)

Our hybrid operation (in-house and independent consultants)

The recruitment team and the support offered

Expertise (1 page per vertical, with color code specific to each division)

Description of the professions recruited

Key skills

Typical customer profiles

Testimonials or case studies (placeholder)

Button/CTA to offers corresponding to this expertise

Job offers

Page with filter by expertise

“Join vorl” option with our internal offers (consultants, recruitment managers, etc.)

Join us

Why work with vorl.

Independent vs. employee path

Tools provided, support, internal training

Highlighting the support team and recruitment managers

Contact

Form

Email + LinkedIn link

Design requirements:

Font: Gazette LT Std or contemporary serif with a strong identity

Color code by division (the background or page elements must match the color of the expertise):

vorl. / vorl.group. → #000000 (black)

vorl.executive. → #2F4F4F (dark green)

vorl.finance&advisory. → #0B1E36 (midnight blue)

vorl.people&office. → #f2b8b8 (powder pink)

vorl.audit&expertise. → #993294 (plum)

vorl.legal. → #d9a00f (yellow gold)

vorl.supply&purchasing. → #CE8946 (rust bronze)

vorl.industry&engineering. → #9e9b9e (light silver gray)

Technical features:

100% responsive and mobile-friendly design

Fast charging

Own structure (SEO-friendly)

Simple back-office interface for updating offers

Language selector FR / EN

Inspirations to consult:

For the tree structure, tabs and ergonomics: tindle-bray.com

For visual ambiance / video / animation: maltevo.ca

Expected deliverables:

Full site (online or compressed file)

All source files (HTML/CSS/JS or custom Wordpress)

Favicon

Brand guideline (PDF) with:

Typographies used

HEX color codes

Margins and line spacing

Examples of use of light and dark background logo

Optional: template for email signature

Objective
Design a modern, elegant and clean website with a touch of sophistication. The site must be fully custom-coded (or built with custom WordPress development), responsive, fast, and reflect the premium standards and quality of our recruitment firm.

It must be bilingual (FR/EN), with a clearly visible language selector in the header.

About vorl.
vorl. is a premium recruitment firm driven by experienced consultants — whether in-house or freelance — supported by a dedicated team of recruitment coordinators. Our hybrid model allows us to handle complex, confidential, or high-volume recruitment assignments with both precision and agility.

We operate across several verticals:

Executive

Finance & Advisory (accounting, controlling, treasury, corporate finance, investment banking advisory)

Legal

Audit & Expertise

People & Office

Supply & Purchasing

Industry & Engineering

Our approach combines human expertise with cutting-edge technologies (AI, automation, data) to tackle recruitment challenges with accuracy, speed, and impact.

Tagline: Expertise serving every recruitment need.

Website Purpose
Client-facing: highlight our expertise, values, and recruitment support model.

Candidate-facing: allow job seekers to explore openings by area of expertise.

Consultant-facing: attract freelance or in-house recruiters to join vorl.

Site Structure & Required Pages
Home
Hero banner with tagline and impactful visual (option for background video, eg maltevo. That)

Clear user path: “I'm looking to hire” / “I want to join vorl. ”

Quick intro to our expertise areas with links to each division page

Highlight our values and unique model

About Us
Our mission

Our hybrid recruitment model (internal consultants + freelancers)

Our recruitment support team and how we work

Expertise (1 page per vertical, using the division's brand color)
Each division page should include:

Description of roles we recruit

Key skills

Typical client profiles

Placeholder for testimonials or success stories

CTA linking to job openings relevant to the division

Verticals:

Executive

Finance & Advisory

Legal

Audit & Expertise

People & Office

Supply & Purchasing

Industry & Engineering

Job Offers
Central job board with filter by expertise

Section: “Join vorl. ” with internal positions (consultants, recruitment coordinators, etc.)

Join Us
Why join vorl.

Independent vs. permanent contract path

Tools, training and operational support

Highlight the internal sourcing and recruitment support team

Contact
Contact form

Email + LinkedIn link

Design Requirements
Font: Gazette LT Std or similar contemporary serif with strong identity

Each vertical should have its own dedicated brand color applied to its page background or key elements:

Division HEX Code Color Description
vorl. /vorl.group. #000000 Black
vorl.executive #2F4F4F Dark green
vorl.finance&advisory #0B1E36 Navy blue
vorl.people&office #f2b8b8 Powder pink
vorl.audit&expertise #993294 Plum
vorl.legal #d9a00f Golden yellow
vorl.supply&purchasing #CE8946 Rust bronze
vorl. industry&engineering #9e9b9e Light silver gray

Technical Features
Fully responsive and mobile-friendly

Fast loading

Clean structure, SEO optimized

Simple back-office interface for job posting and updates

Bilingual switch: FR / EN

Inspirations
For navigation, structure, and user interface:
🔗 https://www.tindle-bray.com/fr/fr/

For visual style, animations, and dynamic video intro:
🔗 https://maltevo.ca/

Deliverables
Fully functional website (live or delivered as a complete package)

All source files (HTML/CSS/JS or custom WordPress)

Favicon

Brand guideline (PDF) including:

Fonts used

HEX color codes

Spacing and layout guidelines

Logo usage on dark/light backgrounds

Optional: email signature template

Target Market(s)

Recruitment firm environment

Industry/Entity Type

Hi, A few clarifications to guide the website structure. The site should be clearly built around three main sections, each addressing a specific target audience: 1. For Clients – “Looking to hire?” This section will highlight our recruitment services, industry expertise, and tailored approach. 2. For Candidates – “Looking for a job?” A space where candidates can explore job offers by sector and apply directly. 3. For Experts – “Want to join us?” This area is for recruitment professionals (consultants or talent acquisition specialists) interested in joining vorl., either as employees or as independents. It should showcase the tools, support, and working environment we offer. These three user paths should be clearly visible on the homepage, using clear buttons or dedicated sections to ensure smooth navigation.

Coding

Coded - Design and coding required

Number of Pages Required

5+ page

Font styles to use
Other font styles liked:
• Gazette LT Std

Colors

Designer to choose colors to be used in the design.

Requirements
Must have
• Essentials – Section Ideas Our hybrid model → Clear presentation of employee/freelance cohabitation, and how it brings flexibility and efficiency to clients. Our quality commitment → Rigorous methodology, transparency, customer satisfaction, tailor-made support. Our augmented approach → Highlighting the use of AI tools, intelligent CRM, automated multi-channel sourcing, predictive tests, etc. Our support team → Promotion of the team of recruitment managers who support the consultants, guaranteeing responsiveness and depth in the hunt. Our areas of expertise → Mini-grid or mosaic that links to the main verticals (useful for cross-functional reinforcement).
Nice to have
• CRM / ATS Integration Direct connection with our application management tool (Velump type or other), for seamless synchronization of offers, applications and follow-ups. 📱 Progressive web app version (PWA) A site accessible in mobile application mode, for a smooth, fast and accessible offline user experience.

```html
<!DOCTYPE html>
<html lang="en">
<head>
<meta charset="UTF-8">
<title>vorl. — Expertise at the service of every recruitment</title>
<link rel="stylesheet" href="https://fonts.googleapis.com/css2?family=Newsreader:opsz,wght@6..72,400;6..72,500;6..72,700&family=Inter:wght@400;500&display=swap">
<style>
  :root{
    --cream:#f7f1e6;
    --glow:#f3cfcc;
    --ink:#1c1a1a;
    --plum:#993294;
    --gold:#d9a00f;
    --powder:#f2b8b8;
    --lavender:#b3b1cc;
    --muted:#7d7a86;
    --nav-bg:rgba(255,250,246,.55);
    --serif:"Newsreader", "Times New Roman", serif;
    --sans:"Inter", Arial, sans-serif;
  }
  *{box-sizing:border-box;margin:0;padding:0}
  html,body{width:1200px;height:706px;overflow:hidden}
  body{
    font-family:var(--sans);color:var(--ink);
    background:
      radial-gradient(ellipse 520px 260px at 600px 40px, rgba(240,190,188,.75), rgba(240,190,188,0) 100%),
      var(--cream);
    position:relative;
  }
  .site-header{
    position:absolute;left:100px;top:23px;width:1000px;height:60px;
    background:var(--nav-bg);border-radius:12px;
  }
  .brand{
    position:absolute;left:20px;top:6px;width:126px;height:48px;
    background:rgba(247,240,222,.8);
    font-family:var(--serif);font-weight:700;font-size:36px;line-height:48px;
    padding-left:20px;letter-spacing:-.5px;color:#111;
  }
  .main-nav{position:absolute;left:179px;top:0;height:60px;display:flex;align-items:center;gap:36px;font-size:14px;font-weight:500}
  .main-nav a{color:#1c1a1a;text-decoration:none}
  .btn{display:inline-flex;align-items:center;justify-content:center;border-radius:5px;font-family:var(--sans);text-decoration:none}
  .btn-primary{background:var(--plum);color:#fff}
  .btn-outline{border:1px solid #3a3838;color:#1c1a1a;background:transparent}
  .header-cta{position:absolute;right:20px;top:8px;width:97px;height:44px;font-size:16px}
  .hero{position:absolute;left:0;top:0;width:1200px;text-align:center}
  .tagline-pill{
    position:absolute;left:444px;top:120px;width:312px;height:32px;
    border:1px solid var(--gold);border-radius:7px;background:#f8f1dc;
    display:flex;align-items:center;gap:8px;padding:0 4px;font-size:14px;
  }
  .tagline-pill .tag{background:var(--powder);border-radius:4px;padding:3px 8px;font-weight:500}
  .hero-title{
    position:absolute;left:0;top:176px;width:1200px;
    font-family:var(--serif);font-weight:400;font-size:60px;line-height:58px;letter-spacing:-1.8px;
  }
  .hero-lead{
    position:absolute;left:320px;top:324px;width:560px;
    font-size:15px;line-height:22px;color:var(--lavender);
  }
  .paths{position:absolute;left:292px;top:415px;height:44px;display:flex;align-items:center}
  .paths-label{font-family:var(--serif);font-size:36px;letter-spacing:-1.2px;margin-right:16px}
  .paths .btn{height:44px;font-size:16px;margin-right:17px}
  .p-hire{width:80px}.p-job{width:79px}.p-join{width:134px}
  .journey{position:absolute;left:0;top:485px;width:1200px;font-size:13px;color:var(--muted)}
  .proof{position:absolute;left:467px;top:520px;display:flex;align-items:center;gap:16px;font-size:15px}
  .avatars{display:flex}
  .avatar{width:34px;height:34px;border-radius:50%;border:2px solid #efe8dc;margin-left:-16px}
  .avatar:first-child{margin-left:0}
  .a1{background:linear-gradient(135deg,#c9b8a8,#8f7868)}
  .a2{background:linear-gradient(135deg,#9fb0c4,#5e6c80)}
  .a3{background:linear-gradient(135deg,#b8a898,#6d5d50)}
  .a4{background:linear-gradient(135deg,#d8c6b4,#7a5a44)}
  .clients{position:absolute;left:0;top:580px;width:1200px;height:40px}
  .client{position:absolute;top:0;display:flex;align-items:center;gap:12px;font-size:24px;font-weight:500;color:#1f1e1e;letter-spacing:-.3px}
  .client .mark{width:32px;height:32px;border-radius:50%}
  .trust{position:absolute;left:0;top:644px;width:1200px;font-size:15px;color:var(--lavender)}
</style>
</head>
<body>
  <header class="site-header">
    <div class="brand">vorl.</div>
    <nav class="main-nav">
      <a href="#">Home</a><a href="#">Expertise</a><a href="#">Job Offers</a><a href="#">Join Us</a><a href="#">About</a><a href="#">Contact</a>
    </nav>
    <a class="btn btn-primary header-cta" href="#">Contact</a>
  </header>

  <main class="hero">
    <div class="tagline-pill"><span class="tag">vorl.</span><span>Your strategic partner in hiring talent.</span></div>
    <h1 class="hero-title">Expertise at the service of<br>every recruitment.</h1>
    <p class="hero-lead">Vorl. is a high-end recruitment firm that blends human insight with cutting-edge technology to deliver precise, impactful hiring solutions.</p>

    <div class="paths">
      <span class="paths-label">Are you looking for :</span>
      <a class="btn btn-primary p-hire" href="#">Hiring</a>
      <a class="btn btn-outline p-job" href="#">A Job</a>
      <a class="btn btn-outline p-join" href="#">Joining Vorl.</a>
    </div>
    <p class="journey">Discover how vorl. can support your journey.</p>

    <div class="proof">
      <div class="avatars">
        <span class="avatar a1" role="img" aria-label="Portrait of a hired candidate"></span>
        <span class="avatar a2" role="img" aria-label="Portrait of a hired candidate"></span>
        <span class="avatar a3" role="img" aria-label="Portrait of a hired candidate"></span>
        <span class="avatar a4" role="img" aria-label="Portrait of a hired candidate"></span>
      </div>
      <span>1290+ Candidates Hired</span>
    </div>

    <div class="clients">
      <div class="client" style="left:150px"><span class="mark" style="background:#8b6cf0"></span>Lumeric</div>
      <div class="client" style="left:337px"><span class="mark" style="background:#f2a27a"></span>Kestrow</div>
      <div class="client" style="left:543px"><span class="mark" style="background:#5b7ff2"></span>Tavelo</div>
      <div class="client" style="left:738px"><span class="mark" style="background:#6f6f74"></span>Harbrook</div>
      <div class="client" style="left:929px"><span class="mark" style="background:#e07ae6"></span>Ondrel</div>
    </div>
    <p class="trust">Many companies worldwide already trust Vorl.</p>
  </main>
</body>
</html>
```